Motor Insurance Quotation - New Quote format / New Template

We are a 40 year old insurance company called 'Velmor Insurance Agency L.L.C' in Dubai, UAE (Our logo / color design can and details can be found on www.velmorgulf.example).

Velmor provides all kinds of insurance solutions for its clients...currently is this modern fast paced world of ever changing technology and increasing competition we need to be ahead of our competitors...

In order to do so, we are in need to re-design our motor insurance quotation format / template and require it to be more attractive, modern and professional.
Since it is a text heavy format, we need it to look aesthetically appealing to our clients.

We would like to see designs that use our color code (as our website / sample quote currently used is attached)..these designs are required in pdf illustrator formats....i have also attached quotation formats used in the existing market. the template and the samples are only for reference and the templates are not to be followed.

UAE

Insurance

• arial

• Aesthetic Design, Insurance details and covers provided in our quote, Velmor logo, color code (details can be found on our website)
• 1 page (short quote) and 2 page (detailed quote) designs to shared...

```html
<!DOCTYPE html>
<html lang="en">
<head>
<meta charset="utf-8">
<title>Motor Insurance Quotation – Velmor Dubai</title>
<link href="https://fonts.googleapis.com/css2?family=Open+Sans:wght@400;600;700&display=swap" rel="stylesheet">
<style>
:root{
  --purple:#6c2a7c;
  --purple-light:#7e4b8f;
  --purple-text:#7b3a8c;
  --row-a:#f2f2f3;
  --row-b:#e8e8ea;
  --ink:#2a2a2a;
  --ink-soft:#444;
  --band:#e6e6e7;
  --page:#ffffff;
  --backdrop:#f4f4f4;
  --rule:#cfcfcf;
}
*{margin:0;padding:0;box-sizing:border-box}
html,body{width:848px;height:1200px;overflow:hidden}
body{background:var(--backdrop);font-family:"Open Sans",Arial,sans-serif;color:var(--ink);position:relative}
.sheet{position:absolute;left:28px;top:28px;width:790px;height:1138px;background:var(--page);box-shadow:0 0 6px rgba(0,0,0,.35)}
.abs{position:absolute}
.table-head{left:37px;top:29px;width:741px;height:40px;background:var(--purple);border-radius:14px;color:#fff;font-weight:700;font-size:17px}
.table-head span{position:absolute;top:8px}
.cover-table{left:51px;top:73px;width:716px}
.row{display:flex;height:26.4px;font-size:12.5px;line-height:26.4px}
.row:nth-child(odd){background:var(--row-a)}
.row:nth-child(even){background:var(--row-b)}
.row.tall{height:52.8px}
.row .c1{width:331px;padding-left:11px;font-weight:700;color:#333}
.row .c2{width:181px;color:var(--ink-soft)}
.row .c3{color:var(--ink-soft)}
.rule{left:37px;width:732px;height:1px;background:var(--rule)}
.note{left:54px;width:712px;text-align:center;font-size:12.5px;line-height:18px;color:#222}
.note.purple{color:var(--purple-text)}
.transfer{left:37px;top:670px;width:742px;height:41px;border:2px solid var(--purple);border-radius:16px;text-align:center;font-weight:700;font-size:12.5px;line-height:37px}
.client-pill{top:782px;width:200px;height:39px;background:var(--purple);border-radius:14px;color:#fff;font-weight:700;font-size:15px;text-align:center;line-height:39px}
.checklist{list-style:none;top:831px;font-size:15px;color:#333}
.checklist li{height:20.6px;display:flex;align-items:center}
.checklist li::before{content:"";width:12px;height:12px;border:1.6px solid var(--purple);border-radius:50%;margin-right:10px}
.footer-band{left:0;top:997px;width:790px;height:28px;background:var(--band)}
.brand{left:46px;top:1001px;font-weight:700;font-size:14px;color:var(--purple)}
.footer-left{left:0;top:1025px;width:395px;height:113px;background:var(--purple);color:#fff;font-size:12px;line-height:17px;padding:9px 0 0 46px}
.footer-right{left:395px;top:1025px;width:395px;height:113px;background:var(--purple-light);color:#fff;font-size:12px;font-weight:700;line-height:17px;padding:9px 0 0 7px}
</style>
</head>
<body>
<div class="sheet">
  <div class="abs table-head">
    <span style="left:96px">Cover</span>
    <span style="left:323px">Coverage / Cost</span>
    <span style="left:594px">Limit</span>
  </div>

  <div class="abs cover-table">
    <div class="row"><div class="c1">Personal Accident Benefits for Driver</div><div class="c2">Included</div><div class="c3">AED 200,000</div></div>
    <div class="row"><div class="c1">Personal Accident Benefits for Passengers</div><div class="c2">Included</div><div class="c3">AED 200,000 per Passenger</div></div>
    <div class="row"><div class="c1">RoadAid Roadside Assistance - Silver Card</div><div class="c2">Included</div><div class="c3">Unlimited (Once every 24 hours)</div></div>
    <div class="row tall"><div class="c1">RoadAid Roadside Assistance - Gold Card</div><div class="c2">Optional / AED 100</div><div class="c3">Registration Service &amp; Off Road<br>Pull Out (8am to 6pm)</div></div>
    <div class="row"><div class="c1">Rent a Car Option</div><div class="c2">Optional / AED 250</div><div class="c3">3 times per year, 10 days each</div></div>
    <div class="row"><div class="c1">Agency Repairs</div><div class="c2">Excluded</div><div class="c3">-</div></div>
    <div class="row"><div class="c1">Off Road Cover</div><div class="c2">Excluded</div><div class="c3">Excess AED 750</div></div>
    <div class="row"><div class="c1">Orange Card</div><div class="c2">Optional / Tariff Attached</div><div class="c3">-</div></div>
    <div class="row"><div class="c1">Territorial Limits</div><div class="c2">Included</div><div class="c3">UAE</div></div>
    <div class="row"><div class="c1">Third Party Bodily Injury</div><div class="c2">Included</div><div class="c3">Unlimited</div></div>
    <div class="row"><div class="c1">Third Party Property Damage</div><div class="c2">Included</div><div class="c3">AED 5,000,000</div></div>
    <div class="row"><div class="c1">Ambulance Cover</div><div class="c2">Included</div><div class="c3">-</div></div>
    <div class="row"><div class="c1">Windscreen Claims</div><div class="c2">Included</div><div class="c3">Excess will apply</div></div>
    <div class="row"><div class="c1">Medical Expenses</div><div class="c2">Included</div><div class="c3">AED 10,000 / Person</div></div>
    <div class="row"><div class="c1">Personal Effects(Theft subject to forcible entry)</div><div class="c2">Included</div><div class="c3">AED 4,000</div></div>
    <div class="row"><div class="c1">Natural Calamities</div><div class="c2">Included</div><div class="c3">-</div></div>
  </div>

  <div class="abs rule" style="top:545px"></div>
  <p class="abs note" style="top:556px">Where the insured requests the replacement of the damaged parts with new parts, the insured shall bear the rates of depreciation i.e. nil for brand new vehicles, 5% for the 2nd year, 10% for the 3rd year, 15% for the 4th year, 20% for the<br>5th year and a maximum of 30% for the 6th year onwards.</p>
  <p class="abs note purple" style="top:622px">An Excess of 10% (besides the normal excess) of the amount of the accident is applicable for drivers who are less than 25 years of age</p>
  <div class="abs transfer">This insurance is non transferrable</div>
  <div class="abs rule" style="top:739px"></div>
  <p class="abs note" style="top:751px">Should you accept the above terms, kindly provide us with the following:</p>

  <div class="abs client-pill" style="left:22px">New Client</div>
  <div class="abs client-pill" style="left:407px">Existing Client</div>
  <ul class="abs checklist" style="left:37px">
    <li>Passport &amp; Visa Copy</li>
    <li>Driving License copy</li>
    <li>Registration Card / Purchase Agreement Copy</li>
    <li>Financing Bank name, if any</li>
    <li>Mobile Number &amp; P.O. Box Number</li>
    <li>Attached Credit Form Copy</li>
  </ul>
  <ul class="abs checklist" style="left:433px">
    <li>Registration Card / Purchase Agreement Copy</li>
    <li>Financing Bank name, if any</li>
    <li>Attached Credit Form Copy</li>
  </ul>

  <div class="abs footer-band"></div>
  <div class="abs brand">Velmor Dubai</div>
  <div class="abs footer-left">
    Harbour View Road, Qasr Tower Bldg.<br>
    P.O. Box 4410, Dubai, UAE<br>
    Tel - +971 4 555 0187&nbsp; Fax - +971 4 555 0193<br>
    info@velmorgulf.example<br>
    www.velmorgulf.example
  </div>
  <div class="abs footer-right">
    Registered Name: Velmor Insurance Agency LLC<br>
    General Agents for Al Saraya National Insurance Co. (PSC)<br>
    Insurance Agents Registration No. 64<br>
    A member of the Velmor Insurance Group
  </div>
</div>
</body>
</html>
```